Menu Design Project for new restauranct concept

Design menu for new restaurant concept called Juniper's Burgers & Dogs. Logo is attached.

Industry/Entity Type

Restaurant

Requirements
Must have
• Menu items and pricing:

Burgers
Snack Burger $3.49
Snack Cheeseburger $3.99
Juniper's signature Burger $4.99
Juniper's signature Cheeseburger $5.49
Burger toppings: bacon, lettuce, tomato, onion, pickle, grilled onions, grilled mushrooms, grilled green peppers, jalapeƱo peppers.

Dogs
Hot Dog $2.99
Bacon Cheese Hot Dog $3.99
Slaw Dog $3.99
Kraut Dog $3.49
Chili Dog $3.99 with or with out cheese
Hot dogs are 100% beef

Other
Grilled Chicken Sandwich $5.99
Grilled Chicken Sandwich with cheese $6.49
(Same toppings as burgers)

French Fries $1.99

Loaded Potatos
The Plain Tater: $4.99 choose from: butter, sour cream, cheese, chives
The Garden Tater: $5.99 choose from: the Basic plus, broccoli & cheese, grilled mushrooms, onions, & peppers
The Carver Tater: $6.99 choose from the Basic/Veggie plus: grilled chicken, chili, Philly cheesesteak, pulled pork.

Drinks
32oz. Drink $1.88
20oz. Drink $1.69

attached logo.
Nice to have
• love to incorporate the woodgrain backgound. It makes the logo look most like a cattle brand, which we like.

```html
<!DOCTYPE html>
<html lang="en">
<head>
<meta charset="utf-8">
<title>Juniper's Burgers &amp; Dogs – Menu</title>
<link rel="stylesheet" href="https://fonts.googleapis.com/css2?family=Roboto:wght@400;500;700&family=Open+Sans:wght@300;400&display=swap">
<style>
  :root {
    --backdrop: #dde4e3;
    --wood-light: #f2d9a4;
    --wood-mid: #e9c98e;
    --ink: #1e1b16;
    --ink-soft: #5a4a36;
    --brown: #7a5426;
    --ornament-cream: #f6ead0;
    --ornament-tan: #b48d56;
    --brand-navy: #2f3a4a;
  }
  * { box-sizing: border-box; margin: 0; padding: 0; }
  html, body { width: 1200px; height: 900px; overflow: hidden; }
  body {
    background: var(--backdrop);
    font-family: "Roboto", Arial, sans-serif;
    color: var(--ink);
    position: relative;
  }
  .sheet {
    position: absolute;
    top: 140px;
    width: 440px;
    height: 620px;
    overflow: hidden;
    background: linear-gradient(100deg, var(--wood-light) 0%, var(--wood-mid) 35%, var(--wood-light) 60%, var(--wood-mid) 100%);
    box-shadow: 0 6px 18px rgba(0,0,0,.18);
  }
  .sheet--cover { left: 140px; }
  .sheet--menu { left: 620px; }

  .ornament {
    position: absolute;
    background: radial-gradient(circle at 50% 50%, var(--ornament-cream) 0%, #d9bd8a 55%, var(--ornament-tan) 100%);
  }
  .half-disc {
    position: absolute;
    border-radius: 50%;
    background: var(--brown);
  }

  /* Cover */
  .cover-label { position: absolute; top: 28px; right: 160px; font-size: 10px; }
  .brand { position: absolute; top: 52px; left: 36px; display: flex; align-items: center; gap: 10px; }
  .brand-disc { width: 46px; height: 46px; border-radius: 50%; border: 3px solid var(--brand-navy); }
  .brand-name { font-weight: 700; font-size: 17px; color: var(--brand-navy); line-height: 1.1; width: 160px; }
  .address { position: absolute; top: 230px; left: 36px; font-size: 9px; line-height: 1.35; }
  .address .phone { font-weight: 500; }

  /* Menu */
  .menu-body { position: absolute; top: 80px; left: 36px; width: 330px; }
  .menu-title { font-size: 15px; font-weight: 700; margin-bottom: 10px; }
  .section { margin-bottom: 9px; }
  .section-title { font-size: 12.5px; font-weight: 500; }
  .note { font-family: "Open Sans", Arial, sans-serif; font-weight: 300; font-size: 8px; color: var(--ink-soft); line-height: 1.25; margin-bottom: 4px; }
  .item { display: flex; justify-content: space-between; font-size: 9px; font-weight: 500; line-height: 1.35; }
  .price { font-family: "Open Sans", Arial, sans-serif; font-weight: 400; font-size: 8.5px; color: var(--ink-soft); }
  .tater { margin-bottom: 3px; }
  .tater .item { font-weight: 400; }
  .delivery { position: absolute; bottom: 40px; right: 30px; font-size: 8.5px; font-weight: 700; }
  .mini-brand { position: absolute; bottom: 62px; right: 30px; display: flex; align-items: center; gap: 5px; }
  .mini-brand .brand-disc { width: 20px; height: 20px; border-width: 2px; }
  .mini-brand .brand-name { font-size: 8px; width: auto; }
</style>
</head>
<body>

<section class="sheet sheet--cover">
  <div class="ornament" style="left:300px;top:0;width:140px;height:470px;border-radius:60px 0 0 40px" role="img" aria-label="Brown line-art mandala ornament running down the right edge"></div>
  <div class="ornament" style="left:0;top:420px;width:440px;height:200px;border-radius:80px 60px 0 0" role="img" aria-label="Mandala flower ornaments along the bottom edge"></div>
  <div class="half-disc" style="left:370px;top:-70px;width:140px;height:140px"></div>
  <div class="half-disc" style="left:380px;top:270px;width:120px;height:120px"></div>
  <div class="half-disc" style="left:-70px;top:470px;width:140px;height:140px"></div>

  <p class="cover-label">Restaurant Menu</p>
  <div class="brand">
    <span class="brand-disc"></span>
    <span class="brand-name">Juniper's Burgers &amp; Dogs</span>
  </div>
  <address class="address" style="font-style:normal">
    1450 Larkspur Avenue, Fairview, MD 21030<br>
    <span class="phone">Tel. 410-555-0187</span><br>
    www.junipersburgers.example
  </address>
</section>

<section class="sheet sheet--menu">
  <div class="ornament" style="left:0;top:0;width:110px;height:80px;border-radius:0 0 60px 0" role="img" aria-label="Mandala ornament in the top-left corner"></div>
  <div class="ornament" style="left:110px;top:0;width:230px;height:60px;border-radius:0 0 50px 50px" role="img" aria-label="Mandala ornaments along the top edge"></div>
  <div class="ornament" style="left:330px;top:0;width:110px;height:270px;border-radius:0 0 0 70px" role="img" aria-label="Mandala ornament in the top-right corner"></div>
  <div class="half-disc" style="left:385px;top:70px;width:110px;height:110px"></div>
  <div class="ornament" style="left:0;top:470px;width:70px;height:150px;border-radius:0 50px 0 0" role="img" aria-label="Mandala ornament in the bottom-left corner"></div>
  <div class="ornament" style="left:70px;top:570px;width:140px;height:50px;border-radius:40px 40px 0 0" role="img" aria-label="Mandala flowers along the bottom edge"></div>

  <div class="menu-body">
    <h1 class="menu-title">Restaurant Menu</h1>

    <div class="section">
      <h2 class="section-title">Burgers</h2>
      <p class="note">Burger toppings: bacon, lettuce, tomato, onion, pickle, grilled onions, grilled mushrooms, grilled green peppers, jalapeño peppers.</p>
      <p class="item"><span>Snack Burger</span><span class="price">$3.49</span></p>
      <p class="item"><span>Snack Cheeseburger</span><span class="price">$3.99</span></p>
      <p class="item"><span>Juniper's signature Burger</span><span class="price">$4.99</span></p>
      <p class="item"><span>Juniper's signature Cheeseburger</span><span class="price">$5.49</span></p>
    </div>

    <div class="section">
      <h2 class="section-title">Dogs</h2>
      <p class="note">Hot dogs are 100% beef</p>
      <p class="item"><span>Hot Dog</span><span class="price">$2.99</span></p>
      <p class="item"><span>Bacon Cheese Hot Dog</span><span class="price">$3.99</span></p>
      <p class="item"><span>Slaw Dog</span><span class="price">$3.99</span></p>
      <p class="item"><span>Kraut Dog</span><span class="price">$3.49</span></p>
      <p class="item"><span>Chili Dog (with or with out cheese)</span><span class="price">$3.99</span></p>
    </div>

    <div class="section">
      <h2 class="section-title">Others</h2>
      <p class="note">(Same toppings as burgers)</p>
      <p class="item"><span>Grilled Chicken Sandwich</span><span class="price">$5.99</span></p>
      <p class="item"><span>Grilled Chicken Sandwich with cheese</span><span class="price">$6.49</span></p>
    </div>

    <div class="section">
      <p class="item"><span class="section-title">French Fries</span><span class="price">$1.99</span></p>
    </div>

    <div class="section">
      <h2 class="section-title">Loaded Potatoes</h2>
      <div class="tater">
        <p class="item"><span>The Plain Tater</span><span class="price">$4.99</span></p>
        <p class="note">choose from: butter, sour cream, cheese, chives</p>
      </div>
      <div class="tater">
        <p class="item"><span>The Garden Tater</span><span class="price">$5.99</span></p>
        <p class="note">choose from: the Basic plus, broccoli &amp; cheese, grilled mushrooms, onions, &amp; peppers</p>
      </div>
      <div class="tater">
        <p class="item"><span>The Carver Tater</span><span class="price">$6.99</span></p>
        <p class="note">choose from the Basic/Veggie plus: grilled chicken, chili, Philly cheesesteak, pulled pork.</p>
      </div>
    </div>

    <div class="section">
      <h2 class="section-title">Drinks</h2>
      <p class="item"><span>32oz. Drink</span><span class="price">$1.88</span></p>
      <p class="item"><span>20oz. Drink</span><span class="price">$1.69</span></p>
    </div>
  </div>

  <div class="mini-brand">
    <span class="brand-disc"></span>
    <span class="brand-name">Juniper's Burgers &amp; Dogs</span>
  </div>
  <p class="delivery">For Home Delivery Please Call on : 410-555-0187</p>
</section>

</body>
</html>
```